Web Site

Target Market(s)

CEOs and International Sales & Marketing Directors of International Companies who wish to expand their business reach to Dubai and the Middle East and are looking for a local professional partner to work with.

Requirements
Must have
• Creativity is key. We don't want the normal standard boxes of text and boxes of pics. Be as creative as you like.
Nice to have
• (This is only a suggestion, we welcome your creativity)
- The center of all pages could be large rotating pictures which display professional corporate men/women working in an office, images of Dubai, the UAE, skyscrapers of business towers in Dubai, ..etc.
- Images should reflect Dubai and the Arab World as a modern, fast-paced, growing modern market - Not Traditional)
Should not have
• Not so colorful, the fewer colors you use, the better.
Not Crammed or Busy
Not Traditional but modern

```html
<!DOCTYPE html>
<html lang="en">
<head>
<meta charset="utf-8">
<title>Halden Group</title>
<link href="https://fonts.googleapis.com/css2?family=Questrial&family=Source+Sans+3:ital,wght@0,400;0,600;1,400;1,600&display=swap" rel="stylesheet">
<style>
:root{
  --maroon:#8e2a24;
  --maroon-dark:#6f1d18;
  --maroon-light:#a8372f;
  --ink:#222;
  --text:#4a4a4a;
  --muted:#6a6a6a;
  --rule:#dcdcdc;
  --page:#f3f3f3;
  --tint:#f7e9ea;
}
*{margin:0;padding:0;box-sizing:border-box}
html,body{width:1200px;height:1181px;overflow:hidden;background:#fff}
body{position:relative;font-family:"Source Sans 3",sans-serif;color:var(--text)}
a{color:inherit;text-decoration:none}
.top-band{position:absolute;left:0;top:0;width:1200px;height:633px;background:linear-gradient(#fdfdfd,#f1f1f1);border-top:3px solid #111}
.utility-bar{position:absolute;left:0;top:3px;width:1200px;height:34px;background:linear-gradient(#fafafa,#ececec);display:flex;justify-content:flex-end;align-items:center;padding-right:90px;font-size:13px;color:var(--maroon)}
.utility-bar span{margin:0 10px;color:var(--maroon)}
.brand{position:absolute;left:50px;top:78px;font-family:"Questrial",sans-serif;font-size:44px;color:var(--ink);letter-spacing:1px}
.search{position:absolute;left:861px;top:97px;display:flex;align-items:center}
.search-field{width:266px;height:33px;background:#fff;border:1px solid #e3e3e3;box-shadow:0 2px 3px rgba(0,0,0,.08);font-style:italic;font-size:12px;color:var(--maroon);padding:9px 10px}
.search-go{width:38px;height:38px;border-radius:50%;background:var(--maroon);color:#fff;font-size:12px;display:flex;align-items:center;justify-content:center;margin-left:-6px}
.main-nav{position:absolute;left:27px;top:173px;width:1141px;height:53px;background:linear-gradient(var(--maroon-light),var(--maroon-dark));border-radius:3px 3px 0 0;display:flex;color:#fff;font-size:16.5px}
.main-nav a{display:flex;align-items:center;justify-content:center;border-right:1px solid rgba(255,255,255,.35)}
.main-nav a:last-child{border-right:0}
.hero{position:absolute;left:27px;top:228px;width:1141px;height:379px;background:#fff;box-shadow:0 3px 6px rgba(0,0,0,.12);overflow:hidden}
.hero-photo{position:absolute;right:0;top:0;width:666px;height:379px;background:linear-gradient(110deg,#f4ece6 0%,#c9a58c 40%,#6d4e3f 70%,#efe9e4 100%)}
.hero-title{position:absolute;left:80px;top:62px;font-family:"Questrial",sans-serif;font-weight:400;font-size:24px;color:#111;white-space:nowrap}
.hero-title em{font-style:normal;color:var(--maroon)}
.hero-sub{position:absolute;left:80px;top:102px;font-family:"Questrial",sans-serif;font-size:19px;color:var(--maroon)}
.hero-rule{position:absolute;left:80px;top:137px;width:290px;height:1px;background:linear-gradient(90deg,#e5c9c9,transparent)}
.hero-body{position:absolute;left:80px;top:150px;width:365px;font-size:13.5px;line-height:21px;color:var(--muted)}
.hero-btn{position:absolute;left:82px;top:229px;width:104px;height:30px;background:#111;color:#fff;border-radius:4px;font-size:14px;display:flex;align-items:center;justify-content:center;gap:6px}
.slider-dots{position:absolute;left:188px;top:306px;display:flex;gap:18px}
.slider-dots i{width:13px;height:13px;border-radius:50%;background:#555}
.slider-dots i:first-child{background:var(--maroon)}
.column{position:absolute;top:660px;width:346px}
.column h2{font-family:"Questrial",sans-serif;font-weight:400;font-size:20px;color:var(--maroon);margin-bottom:14px}
.column h2 b{font-weight:400;color:#111}
.divider{position:absolute;top:660px;width:1px;height:407px;background:var(--rule)}
.welcome-photo{width:341px;height:114px;border-radius:4px;background:linear-gradient(90deg,#3f79b5,#8fb3d4 40%,#b08a6a 70%,#4f8bc4);margin:0 0 20px -4px}
.copy{font-size:13.5px;line-height:20px;color:var(--text)}
.copy p+p{margin-top:20px}
.item{margin-bottom:20px}
.item h3{font-weight:600;font-size:16.5px;color:#444;margin-bottom:6px}
.item.news h3{font-size:13.5px;color:var(--maroon)}
.item p{font-size:13.5px;line-height:20px}
.more{display:block;font-style:italic;font-weight:600;font-size:13px;color:#555;margin-top:5px}
.panel-btn{position:absolute;top:1005px;width:345px;height:31px;background:linear-gradient(90deg,var(--tint),#f6eeee);border-left:3px solid var(--maroon);box-shadow:0 4px 4px -3px rgba(0,0,0,.15);font-weight:600;font-size:13.5px;color:var(--maroon);display:flex;align-items:center;padding-left:11px}
.footer-rule{position:absolute;left:0;top:1079px;width:1200px;height:102px;background:#f8f8f8;border-top:1px solid var(--rule)}
.footer-nav{position:absolute;left:0;top:1104px;width:1200px;text-align:center;font-size:13.5px;color:var(--muted)}
.footer-nav span{margin:0 11px}
.copyright{position:absolute;left:0;top:1138px;width:1200px;text-align:center;font-size:13px;color:var(--muted)}
</style>
</head>
<body>
<div class="top-band"></div>
<nav class="utility-bar"><a href="#">FAQ's</a><span>|</span><a href="#">Support</a><span>|</span><a href="#">Contact info</a></nav>

<div class="brand">Halden Group</div>

<form class="search"><div class="search-field">SEARCH HERE..</div><div class="search-go">GO</div></form>

<nav class="main-nav">
  <a href="#" style="width:106px">Home</a>
  <a href="#" style="width:173px">About the Group</a>
  <a href="#" style="width:191px">Chairman's Message</a>
  <a href="#" style="width:118px">Divisions</a>
  <a href="#" style="width:178px">Group Companies</a>
  <a href="#" style="width:240px">Employment &amp; Association</a>
  <a href="#" style="width:135px">Contact us</a>
</nav>

<section class="hero">
  <div class="hero-photo" role="img" aria-label="Photo of a smiling group of diverse business professionals"></div>
  <h1 class="hero-title">HALDEN GROUP <em>PUCH LINE..</em></h1>
  <p class="hero-sub">tittle line goes here</p>
  <div class="hero-rule"></div>
  <p class="hero-body">It's the simplest, cheapest and also the basic thing the search engine picks it up very easily. We at Brightway tech provide you the best simple websites too.</p>
  <a href="#" class="hero-btn">learn more
    <svg width="8" height="10" viewBox="0 0 8 10"><path d="M2 1l4 4-4 4" fill="none" stroke="#fff" stroke-width="1.8"/></svg></a>
  <div class="slider-dots"><i></i><i></i><i></i><i></i><i></i></div>
</section>

<section class="column" style="left:39px">
  <h2>Welcome to <b>Halden Group</b></h2>
  <div class="welcome-photo" role="img" aria-label="Photo of a video conference meeting room"></div>
  <div class="copy">
    <p>Halden group is a Dubai-based diversified groups of companies led by its chairman Sheikh Rashid bin Khalid Al Noor, a member of the Royal family of Dubai.</p>
    <p>The Group has grown with Dubai, and while best known for Real Estate Investment, it is globally recognized through its involvement in the Legal Consultations, Media Production, General Trading.</p>
  </div>
</section>
<a href="#" class="panel-btn" style="left:39px">READ MORE</a>

<div class="divider" style="left:404px"></div>

<section class="column" style="left:425px">
  <h2>Group Services</h2>
  <div class="item"><h3>Litigation</h3><p>This includes representing Clients and appearing before all courts of different types</p><a href="#" class="more">read more..</a></div>
  <div class="item"><h3>Dispute Resolutions</h3><p>This covers representing clients before arbitration, reconciliation</p><a href="#" class="more">read more..</a></div>
  <div class="item"><h3>Legal Consultations</h3><p>It includes legal consultations in all legal matters</p><a href="#" class="more">read more..</a></div>
</section>
<a href="#" class="panel-btn" style="left:427px">VIEW ALL</a>

<div class="divider" style="left:786px"></div>

<section class="column" style="left:812px">
  <h2>News &amp; Events</h2>
  <div class="item news"><h3>News tittel or Headline</h3><p>It includes expertise and enables Brightway eSolutions to specialize in advanced projects.</p><a href="#" class="more">read more..</a></div>
  <div class="item news"><h3>News tittel or Headline</h3><p>which are usually been used and are benefited through the Professionals and Small Companies.</p><a href="#" class="more">read more..</a></div>
  <div class="item news"><h3>News tittel or Headline</h3><p>It's the simplest, cheapest and also the basic thing</p><a href="#" class="more">read more..</a></div>
</section>
<a href="#" class="panel-btn" style="left:814px">VIEW ALL</a>

<footer>
  <div class="footer-rule"></div>
  <nav class="footer-nav"><a href="#">Home</a><span>|</span><a href="#">About the Group</a><span>|</span><a href="#">Chairman's Message</a><span>|</span><a href="#">Divisions</a><span>|</span><a href="#">Group Companies</a><span>|</span><a href="#">Employment &amp; Association</a><span>|</span><a href="#">Contact us</a></nav>
  <p class="copyright">© 2012 Company Name &nbsp;|&nbsp; All right reserved</p>
</footer>
</body>
</html>
```